*YO!!! Designers Needed!!* Front Page Cover Needed for a $$Billion Dollar$$ Company

We are a manufacturer of aluminum electrolytic capacitors. We are looking to create a front page cover that will be used on our annual report. We are a publicly listed company and work with many Pinnacle 300 companies, so your work will be viewed by the BIG GUNS and EXECUTIVES around the WORLD! If selected, you may be selected for additional work.

The front page cover should be unique. If elegance, modern, bling, and creativity somehow got together and had a child, that's what the cover page would look like!

Inspired Examples attached. Check them out!

www.velmoro.com

Font styles to use
Sans Serif

Requirements
Must have
• 1. Must include the attached logo. Logo size, color, and placement are at your discretion.

2. Should include the text, '2020 Annual Report'

3. The design should incorporate the use of foil and/or be embossed. The foil can be part of the design or can be the full page. See various examples attached for reference.

4. Shall be in A4 size and vertical orientation.
Nice to have
• Feel free to add any icons or stock photos (for example capacitors or circuit boards) if needed.

Be creative here and don't be afraid to be bold! The end product will be printed and budget is not a limiting factor, so feel free to make it extravagant if needed.

Our slogan is "Think Ahead". This slogan can or cannot be part of the theme.

```html
<!DOCTYPE html>
<html lang="en">
<head>
<meta charset="utf-8">
<title>Velmoro Annual Report 2020 Cover</title>
<link href="https://fonts.googleapis.com/css2?family=Titillium+Web:wght@300;400;600&display=swap" rel="stylesheet">
<style>
  :root {
    --backdrop: #4a4a4a;
    --cover: #333333;
    --foil: #62bb9c;
    --emboss: #282828;
  }
  html, body {
    margin: 0;
    padding: 0;
    width: 1199px;
    height: 1200px;
    overflow: hidden;
    background: var(--backdrop);
  }
  .cover {
    position: absolute;
    left: 209px;
    top: 48px;
    width: 780px;
    height: 1103px;
    background: var(--cover);
    font-family: "Titillium Web", sans-serif;
  }
  .spine-line {
    position: absolute;
    left: 387px;
    width: 6px;
    background: var(--foil);
  }
  .spine-line.upper { top: 0; height: 364px; }
  .spine-line.notch { top: 442px; height: 10px; }
  .spine-line.lower { top: 626px; bottom: 0; }
  .title {
    position: absolute;
    left: 211px;
    top: 364px;
    margin: 0;
    font-size: 60px;
    font-weight: 400;
    line-height: 1;
    color: var(--foil);
    letter-spacing: 0.5px;
  }
  .rule {
    position: absolute;
    left: 178px;
    top: 452px;
    width: 439px;
    height: 13px;
    background: var(--foil);
  }
  .year {
    position: absolute;
    left: 180px;
    top: 478px;
    width: 440px;
    height: 160px;
  }
  .year text {
    font-family: "Titillium Web", sans-serif;
    font-weight: 300;
    font-size: 190px;
    fill: none;
    stroke: var(--foil);
    stroke-width: 1.4;
  }
  .brand-name {
    position: absolute;
    left: 420px;
    top: 640px;
    margin: 0;
    font-size: 52px;
    font-weight: 600;
    line-height: 1;
    letter-spacing: 1px;
    color: var(--emboss);
  }
</style>
</head>
<body>
  <main class="cover">
    <div class="spine-line upper"></div>
    <div class="spine-line notch"></div>
    <div class="spine-line lower"></div>

    <h1 class="title">Annual Report</h1>
    <div class="rule"></div>

    <svg class="year" viewBox="0 0 440 160" aria-label="2020">
      <text x="4" y="146" textLength="430" lengthAdjust="spacingAndGlyphs">2020</text>
    </svg>

    <p class="brand-name">Velmoro</p>
  </main>
</body>
</html>
```